Non profit organization looking for new flyers as "leaflets"

Hi, we are looking for new flyers in form "leaflets in German :-)" i've attached our old flyer, we have new logo and thats why we need new and better design smt ... "New: I've so attached the text Regarding the old cards with minor changes "

Industry/Entity Type

Non Profit

Font styles to use
Sans Serif

```html
<!DOCTYPE html>
<html lang="de">
<head>
<meta charset="utf-8">
<title>Lumena Lernwerk – Faltblatt Ambulante Erziehungshilfe</title>
<link rel="stylesheet" href="https://fonts.googleapis.com/css2?family=Lato:wght@400;700;900&family=Archivo:wght@800&family=Caveat:wght@400&display=swap">
<style>
:root{
  --lime:#cddc2c;
  --lime-deep:#a9c824;
  --green:#7fb528;
  --green-dark:#5f8f1e;
  --slate:#2c333a;
  --slate-mid:#4a535c;
  --paper:#ffffff;
  --paper-shade:#eceeef;
  --ink:#2c333a;
}
*{margin:0;padding:0;box-sizing:border-box}
html,body{width:1200px;height:898px;overflow:hidden;background:#e9eaeb}
body{font-family:"Lato",sans-serif;color:var(--ink)}
.leaflet{position:relative;width:1200px;height:898px;display:flex}
.panel{position:relative;width:400px;height:898px;overflow:hidden;background:var(--paper)}
.panel + .panel{border-left:1px solid #d9dcde}
.panel-bg{position:absolute;inset:0}
.brand{position:absolute;display:flex;align-items:center;gap:8px;font-family:"Lato",sans-serif;font-weight:900;color:var(--slate);white-space:nowrap}
.brand-mark{width:14px;height:14px;background:var(--green)}
.photo{position:absolute}
/* left panel */
.intro-brand{left:48px;top:395px;font-size:22px}
.intro-text{position:absolute;left:36px;top:440px;width:328px;font-size:11.5px;line-height:1.45;text-align:center;color:var(--slate)}
.intro-text p + p{margin-top:16px}
.web{position:absolute;left:0;width:400px;text-align:center;color:#fff;font-weight:700;letter-spacing:5px;font-size:14px}
.intro-web{top:852px}
/* middle panel */
.contact-brand{left:50%;transform:translateX(-50%);top:50px;font-size:24px}
.office{position:absolute;font-size:9px;line-height:1.35;color:var(--slate)}
.office strong{display:block;font-size:10px;font-weight:900}
.office-a{left:28px;top:140px}
.office-b{left:220px;top:112px}
.office-c{left:170px;top:400px}
/* cover */
.cover-brand{left:50%;transform:translateX(-50%);top:70px;font-size:30px}
.cover-title{position:absolute;left:0;width:400px;top:628px;display:flex;flex-direction:column;align-items:center;gap:6px}
.cover-title span{font-family:"Archivo",sans-serif;font-weight:800;font-size:30px;line-height:1;color:var(--slate);background:var(--green);padding:5px 12px;letter-spacing:.5px}
.cover-title span:first-child{background:var(--lime-deep)}
.cover-tagline{position:absolute;left:0;width:400px;top:722px;text-align:center;font-family:"Caveat",cursive;font-size:40px;color:var(--slate)}
.cover-web{top:848px}
</style>
</head>
<body>
<main class="leaflet">

  <!-- Panel 1: Einleitung -->
  <section class="panel panel-intro">
    <svg class="panel-bg" viewBox="0 0 400 898" width="400" height="898" aria-hidden="true">
      <defs>
        <linearGradient id="limeFade" x1="0" y1="0" x2="1" y2="1">
          <stop offset="0" stop-color="#d9e43a"/>
          <stop offset="1" stop-color="#b5d12a"/>
        </linearGradient>
      </defs>
      <rect x="0" y="330" width="400" height="568" fill="url(#limeFade)"/>
      <polygon points="0,330 400,300 400,350 0,380" fill="var(--slate)"/>
      <path d="M0 832 Q200 808 400 790 L400 898 L0 898 Z" fill="var(--slate)"/>
    </svg>
    <svg class="photo" style="left:0;top:0" width="400" height="330" role="img" aria-label="Foto: viele Hände verschiedener Hautfarben übereinander, darüber das Wort Team in mehreren Sprachen">
      <defs>
        <linearGradient id="handsTone" x1="0" y1="0" x2="1" y2="1">
          <stop offset="0" stop-color="#d9c2b8"/>
          <stop offset=".5" stop-color="#a9705a"/>
          <stop offset="1" stop-color="#6b4535"/>
        </linearGradient>
      </defs>
      <polygon points="0,0 400,0 400,300 0,330" fill="url(#handsTone)"/>
    </svg>
    <div class="brand intro-brand"><span class="brand-mark"></span>Lumena Lernwerk e.V.</div>
    <div class="intro-text">
      <p>Lorem Ipsum is simply dummy text of the printing and typesetting industry. Lorem Ipsum has been the industry's standard dummy text ever since the 1500s, when an unknown printer took a galley of type and scrambled it to make a type specimen book. It has survived not only five centuries, but also the leap into electronic typesetting, remaining essentially unchanged. It was popularised in the 1960s with the release of Letraset sheets containing Lorem Ipsum passages, and more recently with desktop publishing software like Aldus PageMaker including versions of Lorem Ipsum.</p>
      <p>Lorem Ipsum is simply dummy text of the printing and typesetting industry. Lorem Ipsum has been the industry's standard dummy text ever since the 1500s, when an unknown printer took a galley of type and scrambled it to make a type specimen book. It has survived not only five centuries, but also the leap into electronic typesetting, remaining essentially unchanged.</p>
    </div>
    <div class="web intro-web">WWW.LUMENA-LERNWERK.DE</div>
  </section>

  <!-- Panel 2: Standorte -->
  <section class="panel panel-contact">
    <svg class="panel-bg" viewBox="0 0 400 898" width="400" height="898" aria-hidden="true">
      <defs>
        <linearGradient id="limeWave" x1="0" y1="0" x2="1" y2="0">
          <stop offset="0" stop-color="#c3d82c"/>
          <stop offset="1" stop-color="#a9c824"/>
        </linearGradient>
      </defs>
      <path d="M0 480 Q200 455 400 470 L400 898 L0 898 Z" fill="var(--slate-mid)"/>
      <path d="M0 505 Q200 480 400 495 L400 840 Q200 780 0 800 Z" fill="url(#limeWave)"/>
      <path d="M0 800 Q200 780 400 840 L400 898 L0 898 Z" fill="var(--slate-mid)"/>
      <polygon points="70,545 340,510 330,760 60,745" fill="var(--slate)"/>
      <line x1="60" y1="190" x2="130" y2="235" stroke="#6a6f74" stroke-width="3"/>
      <polygon points="130,235 117,234 124,224" fill="#6a6f74"/>
      <line x1="205" y1="170" x2="210" y2="225" stroke="#6a6f74" stroke-width="3"/>
      <polygon points="210,233 203,220 216,220" fill="#6a6f74"/>
      <line x1="230" y1="390" x2="190" y2="330" stroke="#6a6f74" stroke-width="3"/>
      <polygon points="186,323 197,331 186,337" fill="#6a6f74"/>
    </svg>
    <div class="brand contact-brand"><span class="brand-mark"></span>Lumena Lernwerk e.V.</div>
    <div class="office office-a"><strong>Lumena Lernwerk e.V.</strong>Lindenweg 4 · 10115 Musterstadt<br>Telefon: (0 12 34) 56 78 01<br>Telefax: (0 12 34) 56 78 02</div>
    <div class="office office-b"><strong>Lumena Lernwerk e.V.</strong>Birkenallee 3 · 20095 Neustadt<br>Telefon: (0 98 76) 543 21 25<br>Telefax: (0 98 76) 543 21 26</div>
    <svg class="photo" style="left:105px;top:220px" width="190" height="160" role="img" aria-label="Landkarte der Region mit den drei Standorten">
      <rect width="190" height="160" rx="18" fill="#8f9295"/>
    </svg>
    <div class="office office-c"><strong>Lumena Lernwerk e.V.</strong>Uferstraße 39 · 30159 Altdorf<br>Telefon: (0 45 67) 890 12 77<br>Telefax: (0 45 67) 890 13 02</div>
    <svg class="photo" style="left:0;top:0" width="400" height="898" role="img" aria-label="Foto: Tischtelefon mit Hörer">
      <defs>
        <linearGradient id="phoneTone" x1="0" y1="0" x2="1" y2="1">
          <stop offset="0" stop-color="#c9cdd1"/>
          <stop offset=".55" stop-color="#5a636c"/>
          <stop offset="1" stop-color="#e6e8ea"/>
        </linearGradient>
      </defs>
      <polygon points="85,560 325,528 316,745 76,732" fill="url(#phoneTone)"/>
    </svg>
  </section>

  <!-- Panel 3: Titelseite -->
  <section class="panel panel-cover">
    <svg class="panel-bg" viewBox="0 0 400 898" width="400" height="898" aria-hidden="true">
      <defs>
        <linearGradient id="coverPaper" x1="0" y1="0" x2="1" y2="0">
          <stop offset="0" stop-color="var(--paper-shade)"/>
          <stop offset=".5" stop-color="#ffffff"/>
          <stop offset="1" stop-color="var(--paper-shade)"/>
        </linearGradient>
        <linearGradient id="coverLime" x1="0" y1="0" x2="1" y2="1">
          <stop offset="0" stop-color="#dbe63e"/>
          <stop offset="1" stop-color="#b2cf28"/>
        </linearGradient>
      </defs>
      <rect width="400" height="898" fill="url(#coverPaper)"/>
      <polygon points="0,490 200,600 400,470 400,810 0,810" fill="url(#coverLime)"/>
      <polygon points="0,480 200,600 400,460 400,485 200,615 0,505" fill="var(--green-dark)" opacity=".55"/>
      <polygon points="200,150 400,300 400,440 200,600 0,440 0,300" fill="var(--green)"/>
      <rect x="0" y="810" width="400" height="88" fill="var(--slate)"/>
    </svg>
    <svg class="photo" style="left:0;top:0" width="400" height="620" role="img" aria-label="Foto: zwei nachdenkliche Kinder, die Köpfe auf die Hände gestützt">
      <defs>
        <linearGradient id="kidsTone" x1="0" y1="0" x2="1" y2="1">
          <stop offset="0" stop-color="#d8b878"/>
          <stop offset=".45" stop-color="#6f8a4a"/>
          <stop offset="1" stop-color="#4a5468"/>
        </linearGradient>
      </defs>
      <polygon points="200,168 390,305 390,435 200,582 10,435 10,305" fill="url(#kidsTone)"/>
    </svg>
    <div class="brand cover-brand"><span class="brand-mark"></span>Lumena Lernwerk e.V.</div>
    <h1 class="cover-title"><span>AMBULANTE</span><span>ERZIEHUNGSHILFE</span></h1>
    <div class="cover-tagline">lorem ipsum</div>
    <div class="web cover-web">WWW.LUMENA-LERNWERK.DE</div>
  </section>

</main>
</body>
</html>
```